VelmoraHub

Hey

I am involved with crowd funding, please look at one of my current sites www.funsprell.com
Work is currently under way with a new site www.velmorahub.com .wehave the basics but I am not happy with what we have so far. I need to redesign the web site but keep the concept . The cartoon pitch will be kept , along with some of the other functions which we can help you with, unless you are able to build / design something better. I liked a lot of the designs submitted for a previous crowd funning design, far better than what I currently have. To be included on this site will be links to numerous crowd funding sites which I have registered but each site will be focused on a specific topic which will be disclosed once this site is active. I intend to build all these sites through this site. Along with these sites will be a logo design for each site so plenty of work going forward. I have a logo for velmorahub already but am open for improvements and suggestions but would like to keep a map or logo of Africa included in the design. To bear in mind this is a African focused buisness which aims to help communities, employment creation, poverty alleviation and help young entrepreneurs kickstarter their buisness . I already have a group logo , which was designed on this site ( look at tandel yards competition) , I would like this logo to be used on all the site so customers and investors link the group and concept togeather. Here is the link http://www.brievoshop.co.uk/project-progress.aspx?briefId=48213 . I have removed the tandelyard from the bottom of the logo and will just be using the figurines as the group logo on all web sites. There will be at least fifty related crowd fund projects linked to this site.
If any body has any questions or ideas please feel free to ask for anything you may need. Thanks to everybody who helps with this project. Warmly. Ravi

Hi everyone working on my design.

The contact details to use on the site are

27 Weltmore Close
Dunvale
Cape Town 
+263748395026
+447913462058

E mail enquiries@VelmoraHub.example

There are two logos, one is the velmorahub logo and the other is my group logo which I will attach to the pitch
Good luck and thank you to everybody who is working on this web design
Warmly

Ravi

```html
<!DOCTYPE html>
<html lang="en">
<head>
<meta charset="utf-8">
<title>VelmoraHub – Equity Crowdfunding</title>
<link rel="stylesheet" href="https://fonts.googleapis.com/css2?family=Arimo:wght@400;700&family=Tinos&family=Oswald:wght@400&display=swap">
<style>
:root{
  --ink:#333;
  --muted:#555;
  --blue:#1a8fd1;
  --blue-dark:#0f6fae;
  --link:#1777c4;
  --green:#6bb33a;
  --green-text:#7cb518;
  --page:#e9eef5;
  --band:#f3f5f8;
  --dark:#2b2b2b;
  --line:#d8dde3;
  --white:#fff;
}
*{box-sizing:border-box;margin:0;padding:0}
html,body{width:943px;height:1200px;overflow:hidden}
body{position:relative;background:var(--page);font-family:Arimo,Arial,sans-serif;color:var(--ink);font-size:10px}
.abs{position:absolute}
a{color:inherit;text-decoration:none}

/* top strip */
.topbar{left:0;top:0;width:943px;height:26px;background:var(--white)}
.topbar-links{left:350px;top:0;height:26px;width:416px;background:#3a3a3a;display:flex;align-items:center;color:#eee;font-size:8.5px;white-space:nowrap}
.topbar-links span{padding:0 4px}
.topbar-links .sep{padding:0;color:#888}
.topbar-links .strong{font-weight:700}
.topbar-links .active{background:#555;height:26px;display:flex;align-items:center;padding:0 6px}

/* header */
.header{left:0;top:26px;width:943px;height:82px;background:var(--white)}
.logo{left:178px;top:44px;display:flex;align-items:center;gap:8px}
.logo-mark{width:34px;height:34px;border-radius:50%;background:var(--green)}
.logo-name{font-size:24px;font-weight:700;color:var(--blue-dark);line-height:1}
.logo-tag{left:292px;top:72px;font-size:6.5px;font-weight:700;color:#333;letter-spacing:.4px}
.hbtn{top:34px;height:19px;border-radius:3px;font-size:8.5px;font-weight:700;color:#fff;display:flex;align-items:center;justify-content:center;white-space:nowrap}
.hbtn-social{left:464px;width:114px;background:linear-gradient(#5a79b8,#3b5a98)}
.hbtn-signup{left:581px;width:72px;background:linear-gradient(#9ccb4e,#6f9e27)}
.hbtn-login{left:658px;width:104px;background:linear-gradient(#9ccb4e,#6f9e27)}
.phones{left:690px;top:61px;font-size:8.5px;font-weight:700;letter-spacing:1.2px;line-height:13px;color:#222}
.email{left:640px;top:87px;font-size:9.5px;color:#333;white-space:nowrap}

/* nav */
.nav{left:0;top:108px;width:943px;height:28px;background:linear-gradient(#35a6e4,#1577bd);border-bottom:3px solid #0d5d96}
.nav-links{left:178px;top:115px;color:#fff;font-size:9.5px;font-weight:700;white-space:nowrap}
.search{left:612px;top:113px;width:150px;height:18px;border-radius:3px;background:#fff;font-size:9px;color:#666;padding:4px 8px}

/* slider */
.slider{left:178px;top:142px;width:586px;height:174px;background:#fff;border:1px solid #ccd;border-radius:4px}
.slider-photo{left:184px;top:146px;width:574px;height:120px;background:linear-gradient(#f4f4f4,#c9ccd3 60%,#8b8f99)}
.slider-caption{left:205px;top:274px;width:530px;text-align:center;font-family:Tinos,"Times New Roman",serif;font-size:11px;line-height:12.5px;color:#333}
.arrow{top:278px;width:20px;height:24px;background:#333;border-radius:4px}
.arrow-l{left:162px}.arrow-r{left:763px}
.welcome{left:0;top:322px;width:943px;text-align:center;font-size:21px;font-weight:700;color:var(--blue)}

/* intro band */
.band{left:0;top:355px;width:943px;height:173px;background:var(--band);border-top:1px solid #dde;border-bottom:1px solid #dde}
.intro-title{left:178px;top:375px;font-size:16px;font-weight:700;color:#222;white-space:nowrap}
.intro-text{left:177px;top:401px;width:175px;font-size:9px;line-height:13.5px;color:#444;text-align:justify;letter-spacing:-.1px}
.watch{left:178px;top:469px;font-size:9px;font-weight:700;color:var(--link);white-space:nowrap}
.pill{top:496px;height:20px;border-radius:10px;font-size:8.5px;font-weight:700;display:flex;align-items:center;justify-content:center;white-space:nowrap}
.pill-learn{left:189px;width:82px;background:#e4eff6;border:1px solid #b8cfdd;color:#557}
.pill-join{left:271px;width:72px;background:linear-gradient(#3d8fd4,#1b5fa7);color:#fff}
.video{left:373px;top:382px;width:192px;height:122px;background:linear-gradient(#8a8a8a,#5a5a5a);border:3px solid #333}
.promo{width:172px;color:#fff}
.promo-join{left:592px;top:382px;height:112px;background:var(--blue)}
.promo-fund{left:592px;top:542px;height:104px;background:var(--green)}
.promo h3{position:absolute;left:9px;top:7px;font-family:Oswald,sans-serif;font-weight:400;font-size:19px}
.promo p{position:absolute;left:10px;top:35px;width:120px;font-size:8.5px;line-height:10px}
.promo-fund p{top:33px}
.promo-btn{left:681px;top:468px;width:74px;height:18px;border-radius:9px;background:linear-gradient(#4aa1e0,#1e6bb8);border:1px solid #fff;color:#fff;font-size:8.5px;font-weight:700;display:flex;align-items:center;justify-content:center}
.read-more{position:absolute;left:10px;top:89px;font-size:8.5px;font-weight:700;font-style:italic}
.fund-badge{left:740px;top:553px;width:28px;height:28px;border-radius:50%;background:#fff}

/* project cards */
.card{width:186px;height:190px;background:#fff;border:1px solid var(--line);border-radius:3px}
.card-head{height:26px;background:linear-gradient(#555,#2e2e2e);color:#fff;font-size:10px;text-align:center;line-height:26px;border-radius:3px 3px 0 0;white-space:nowrap}
.card-title{position:absolute;left:11px;top:36px;font-size:9.5px;font-weight:700;color:var(--link)}
.card-text{position:absolute;left:11px;top:51px;width:164px;font-size:8.5px;line-height:10px;color:#444;text-align:justify}
.card-more{position:absolute;left:10px;top:98px;width:36px;height:12px;border:1px solid #bbb;border-radius:2px;background:#f1f1f1;font-size:8px;text-align:center;line-height:10px}
.stat{position:absolute;left:0;width:184px;border-top:1px solid #e2e2e2;display:flex;align-items:center}
.stat-count{top:117px;height:33px}
.stat-funded{top:150px;height:22px}
.stat-goal{top:172px;height:17px}
.stat .label{width:43px;padding-left:7px;font-size:9px;font-weight:700;color:var(--green-text)}
.stat .value{font-size:9px;color:#222}
.stat .count{font-size:15px;color:#222}
.people{margin-left:7px;margin-right:12px}

/* categories */
.cat-title{left:592px;top:662px;font-size:12px;font-weight:700;color:var(--blue)}
.cat-rule{left:592px;top:683px;width:172px;height:2px;background:var(--blue)}
.cat-list{left:592px;top:699px;width:106px;list-style:none}
.cat-list li{height:18px;border-bottom:1px solid #ccd;border-left:2px solid #999;padding-left:5px;font-size:8.5px;line-height:18px;color:#555;white-space:nowrap}
.cat-list li.current{color:var(--green-text);font-weight:700}

/* footer */
.footer{left:0;top:972px;width:943px;height:198px;background:var(--dark);border-top:6px solid #444}
.f-head{top:998px;font-size:11px;font-weight:700;color:#fff}
.f-links{top:1025px;font-size:8.5px;line-height:19px;color:#ddd;white-space:nowrap}
.field{left:571px;width:194px;background:#fff;font-size:8.5px;color:#444;padding:4px 12px}
.submit{left:694px;top:1104px;width:72px;height:18px;border-radius:9px;background:#dfeef5;color:#2c7db8;font-size:8.5px;font-weight:700;display:flex;align-items:center;justify-content:center}
.social{top:1136px;width:17px;height:17px;border-radius:2px}
.copybar{left:0;top:1170px;width:943px;height:30px;background:#f1f1f1;text-align:center;font-size:8.5px;line-height:30px;color:#333}
.copybar .link{color:var(--link)}
</style>
</head>
<body>

<div class="abs topbar"></div>
<nav class="abs topbar-links">
  <span>Blogs</span><span class="sep">|</span><span>IPO's</span><span class="sep">|</span><span>How it Works</span><span class="sep">|</span><span class="active">About VelmoraHub</span>
  <span style="margin-left:6px">Welcome Guest!</span><span class="sep">|</span><span>My Account</span><span class="sep">|</span><span>Wishlist</span><span class="sep">|</span><span class="strong">Register</span><span class="strong" style="padding-left:0">Sign In</span>
</nav>

<header class="abs header"></header>
<div class="abs logo"><span class="logo-mark"></span><span class="logo-name">VelmoraHub</span></div>
<div class="abs logo-tag">EQUITY CROWDFUNDING</div>
<a class="abs hbtn hbtn-social">Sign In with Linkora</a>
<a class="abs hbtn hbtn-signup">Sign Up Today</a>
<a class="abs hbtn hbtn-login">Login to your Account</a>
<svg class="abs" style="left:667px;top:63px" width="14" height="14" viewBox="0 0 14 14"><rect width="14" height="14" rx="3" fill="#2a8fd1"/><path d="M4 3l2 0 1 2-1 1c1 2 1 2 2 2l1-1 2 1v2c-4 1-8-3-7-7z" fill="#fff"/></svg>
<div class="abs phones">+263748395026<br>+447913462058</div>
<svg class="abs" style="left:624px;top:88px" width="12" height="9" viewBox="0 0 12 9"><rect x=".5" y=".5" width="11" height="8" fill="none" stroke="#444"/><path d="M.5 .5l5.5 4 5.5-4" fill="none" stroke="#444"/></svg>
<div class="abs email">enquiries@VelmoraHub.example</div>

<div class="abs nav"></div>
<div class="abs nav-links">Home &nbsp;|&nbsp; Company Info &nbsp;|&nbsp; Join Now! &nbsp;|&nbsp; How it works? &nbsp;|&nbsp; Browse Companies</div>
<div class="abs search">search...</div>
<svg class="abs" style="left:746px;top:117px" width="10" height="10" viewBox="0 0 10 10"><circle cx="4" cy="4" r="3" fill="none" stroke="#888" stroke-width="1.4"/><path d="M6.5 6.5l3 3" stroke="#888" stroke-width="1.6"/></svg>

<section class="abs slider"></section>
<div class="abs slider-photo" role="img" aria-label="Group photograph of smiling business people and entrepreneurs"></div>
<p class="abs slider-caption">Ground rules are simple; JOIN, send us a Vidstream or any other video link to any idea. It can be an idea just floating around or an idea which has already come to life. No catches, no entry fee, no award collection fee,<br>only one entry per member.</p>
<div class="abs arrow arrow-l"></div>
<div class="abs arrow arrow-r"></div>
<svg class="abs" style="left:166px;top:284px" width="12" height="12" viewBox="0 0 12 12"><path d="M8 2L4 6l4 4" fill="none" stroke="#fff" stroke-width="2"/></svg>
<svg class="abs" style="left:767px;top:284px" width="12" height="12" viewBox="0 0 12 12"><path d="M4 2l4 4-4 4" fill="none" stroke="#fff" stroke-width="2"/></svg>
<h1 class="abs welcome">Welcome to Africa’s leading crowdfunding site</h1>

<section class="abs band"></section>
<h2 class="abs intro-title">What is Crowdfunding?</h2>
<p class="abs intro-text">Crowdfunding enables people to raise money for innovative new projects by getting like-minded individuals to pool their money to back the idea, person or business. It's a way to make things happen.</p>
<a class="abs watch">WATCH THE VIDEO</a>
<a class="abs pill pill-learn">Learn more here</a>
<a class="abs pill pill-join">Join Now!</a>
<div class="abs video" role="img" aria-label="Cartoon pitch video player"></div>

<div class="abs promo promo-join">
  <h3>JOIN NOW!</h3>
  <p>Adipiscing elit. Curabitur eu interdum dui. Aliquam turpis mauris, rhoncus et tempus ac, pellentesque quis sem. Nullam a leo arcu, in posuere leo.</p>
</div>
<a class="abs promo-btn">Join Now!</a>

<div class="abs promo promo-fund">
  <h3>FUND</h3>
  <p>Adipiscing elit. Curabitur eu interdum dui. Aliquam turpis mauris, rhoncus et tempus ac, pellentesque quis sem. Nullam a leo arcu, in posuere leo.</p>
  <span class="read-more">Read more...</span>
</div>
<div class="abs fund-badge"></div>
<svg class="abs" style="left:748px;top:559px" width="12" height="16" viewBox="0 0 12 16"><path d="M9 3H4.5a2.3 2.3 0 000 4.6h3a2.3 2.3 0 010 4.6H3M6 1v14" fill="none" stroke="#6bb33a" stroke-width="2"/></svg>

<article class="abs card" style="left:178px;top:544px">
  <div class="card-head">Russia</div>
  <div class="card-title">Lorem ipsum dolor sit amet,</div>
  <p class="card-text">Adipiscing elit. Curabitur eu interdum dui. Aliquam turpis mauris, rhoncus et tempus ac, pellentesque quis sem. Nullam a leo arcu, in posuere leo.</p>
  <div class="card-more">more</div>
  <div class="stat stat-count"><svg class="people" width="24" height="14" viewBox="0 0 24 14"><g fill="#6bb33a"><circle cx="5" cy="4" r="2.5"/><circle cx="12" cy="3" r="3"/><circle cx="19" cy="4" r="2.5"/><path d="M1 13c0-4 8-4 8 0zM7 13c0-5 10-5 10 0zM15 13c0-4 8-4 8 0z"/></g></svg><span class="count">0</span></div>
  <div class="stat stat-funded"><span class="label">Funded</span><span class="value">$0.00</span></div>
  <div class="stat stat-goal"><span class="label">Goal</span><span class="value">$3000.00</span></div>
</article>

<article class="abs card" style="left:378px;top:544px">
  <div class="card-head">Middle East</div>
  <div class="card-title">Lorem ipsum dolor sit amet,</div>
  <p class="card-text">Adipiscing elit. Curabitur eu interdum dui. Aliquam turpis mauris, rhoncus et tempus ac, pellentesque quis sem. Nullam a leo arcu, in posuere leo.</p>
  <div class="card-more">more</div>
  <div class="stat stat-count"><svg class="people" width="24" height="14" viewBox="0 0 24 14"><g fill="#6bb33a"><circle cx="5" cy="4" r="2.5"/><circle cx="12" cy="3" r="3"/><circle cx="19" cy="4" r="2.5"/><path d="M1 13c0-4 8-4 8 0zM7 13c0-5 10-5 10 0zM15 13c0-4 8-4 8 0z"/></g></svg><span class="count">0</span></div>
  <div class="stat stat-funded"><span class="label">Funded</span><span class="value">$0.00</span></div>
  <div class="stat stat-goal"><span class="label">Goal</span><span class="value">$3000.00</span></div>
</article>

<article class="abs card" style="left:178px;top:748px">
  <div class="card-head">Eastern Europe</div>
  <div class="card-title">Lorem ipsum dolor sit amet,</div>
  <p class="card-text">Adipiscing elit. Curabitur eu interdum dui. Aliquam turpis mauris, rhoncus et tempus ac, pellentesque quis sem. Nullam a leo arcu, in posuere leo.</p>
  <div class="card-more">more</div>
  <div class="stat stat-count"><svg class="people" width="24" height="14" viewBox="0 0 24 14"><g fill="#6bb33a"><circle cx="5" cy="4" r="2.5"/><circle cx="12" cy="3" r="3"/><circle cx="19" cy="4" r="2.5"/><path d="M1 13c0-4 8-4 8 0zM7 13c0-5 10-5 10 0zM15 13c0-4 8-4 8 0z"/></g></svg><span class="count">0</span></div>
  <div class="stat stat-funded"><span class="label">Funded</span><span class="value">$0.00</span></div>
  <div class="stat stat-goal"><span class="label">Goal</span><span class="value">$3000.00</span></div>
</article>

<article class="abs card" style="left:378px;top:748px">
  <div class="card-head">Gache Gache Reserve, Zimbabwe</div>
  <div class="card-title">Lorem ipsum dolor sit amet,</div>
  <p class="card-text">Adipiscing elit. Curabitur eu interdum dui. Aliquam turpis mauris, rhoncus et tempus ac, pellentesque quis sem. Nullam a leo arcu, in posuere leo.</p>
  <div class="card-more">more</div>
  <div class="stat stat-count"><svg class="people" width="24" height="14" viewBox="0 0 24 14"><g fill="#6bb33a"><circle cx="5" cy="4" r="2.5"/><circle cx="12" cy="3" r="3"/><circle cx="19" cy="4" r="2.5"/><path d="M1 13c0-4 8-4 8 0zM7 13c0-5 10-5 10 0zM15 13c0-4 8-4 8 0z"/></g></svg><span class="count">5</span></div>
  <div class="stat stat-funded"><span class="label">Funded</span><span class="value">$5.00</span></div>
  <div class="stat stat-goal"><span class="label">Goal</span><span class="value">$100.00</span></div>
</article>

<h3 class="abs cat-title">Business Categories</h3>
<div class="abs cat-rule"></div>
<ul class="abs cat-list">
  <li>Comics</li><li>Environment</li><li>Fashion</li><li>Film &amp; Video</li><li>Gaming</li><li>Health &amp; Fitness</li><li>Music</li><li>Professional Services</li><li>Technology</li><li>More links</li><li class="current">Internet &amp; IT</li><li>Leasure &amp; Tourism</li>
</ul>

<footer class="abs footer"></footer>
<div class="abs f-head" style="left:178px">About Us</div>
<div class="abs f-links" style="left:178px">About US<br>Join Now<br>How it works<br>Privacy policy<br>Our Blog</div>
<div class="abs f-links" style="left:258px">Resources<br>FAQ<br>Email Us<br>My Account<br>Sign Up now</div>
<div class="abs f-head" style="left:376px">Contact Us</div>
<div class="abs f-links" style="left:376px">Phone: +263748395026<br>Fax: &nbsp;&nbsp;&nbsp;&nbsp;&nbsp;+447913462058<br>enquiries@VelmoraHub.example<br>27 Weltmore Close, Dunvale, Cape Town</div>
<div class="abs f-head" style="left:571px">Comments &amp; Feedback</div>
<div class="abs field" style="top:1017px;height:18px">Enter your name</div>
<div class="abs field" style="top:1038px;height:18px">Enter your email here</div>
<div class="abs field" style="top:1059px;height:36px">Message</div>
<a class="abs submit">Submit</a>
<div class="abs" style="left:178px;top:1126px;width:36px;height:36px;border-radius:50%;background:#7a8a2a"></div>
<div class="abs" style="left:216px;top:1134px;width:76px;height:18px;background:#3f9a3a"></div>
<div class="abs" style="left:304px;top:1130px;width:76px;height:26px;border-radius:3px;background:#e8e8e8"></div>
<div class="abs" style="left:398px;top:1130px;width:60px;height:26px;border-radius:13px;background:#f2f2f2"></div>
<div class="abs social" style="left:571px;background:#3b5998"></div>
<div class="abs social" style="left:595px;background:#2fa8e0"></div>
<div class="abs social" style="left:619px;background:#1a77b0"></div>
<div class="abs social" style="left:643px;background:#d0242b"></div>
<div class="abs social" style="left:667px;background:#c7c7c7"></div>
<div class="abs social" style="left:691px;background:#e6e6e6"></div>
<div class="abs social" style="left:715px;background:#26a65b"></div>
<div class="abs copybar">Copyright 2012 Velmora Hub &nbsp;/&nbsp;&nbsp; Use of this website constitutes acceptance of our <span class="link">User Agreement</span> and <span class="link">Privacy Policy</span></div>

</body>
</html>
```